Corvallin Property Solutions need a business card design

Hello guys. We would need a business card design asap please.
We are a start up property investment business based in London UK specialised in buying, selling, managing and letting properties and helping distressed property owners.
The name of our Business is Corvallin, the logo symbolises the four fundamental elements of the world (earth, air, fire and water) and so it stands for strength, stability, longevity.
We would like the business card to communicate professionalism and reliability. Many many thanks indeed for your work.

Details:

1.) Marisol Dunkley
Property Investor
Mobile: +44(0)7700362517
Email: marisol.corvallin@quilbrook.example

2.) Tomas Brindle
Property Investor
Mobile: +44(0)7700845926
Email: tomas.corvallin@quilbrook.example

Industry/Entity Type

Investment

```html
<!DOCTYPE html>
<html lang="en">
<head>
<meta charset="utf-8">
<title>Corvallin Property Solutions – Business Card</title>
<link rel="stylesheet" href="https://fonts.googleapis.com/css2?family=Montserrat:wght@300;400;700;800&display=swap">
<style>
  :root {
    --page-bg: #e4e4e2;
    --card-bg: #efefee;
    --ink: #1c1c1c;
    --ink-soft: #3a3a3a;
    --accent-red: #d0202e;
    --accent-green: #1a9a3c;
    --accent-blue: #1d5fc4;
    --card-shadow: 0 10px 28px rgba(0,0,0,0.16);
  }
  * { box-sizing: border-box; margin: 0; padding: 0; }
  html, body {
    width: 1200px;
    height: 900px;
    overflow: hidden;
    background: var(--page-bg);
    font-family: "Montserrat", sans-serif;
    color: var(--ink);
  }
  .sheet {
    width: 1200px;
    height: 900px;
    display: flex;
    align-items: center;
    justify-content: center;
    gap: 44px;
  }
  .card {
    position: relative;
    width: 520px;
    height: 297px;
    background: var(--card-bg);
    box-shadow: var(--card-shadow);
    overflow: hidden;
  }

  /* Reverse side: brand name */
  .card--reverse {
    display: flex;
    align-items: center;
    justify-content: center;
    gap: 16px;
  }
  .reverse-mark {
    width: 22px;
    height: 22px;
    background: var(--ink);
  }
  .reverse-name {
    font-weight: 800;
    font-size: 40px;
    letter-spacing: 0.06em;
    text-transform: uppercase;
    color: var(--ink);
  }

  /* Front side */
  .brand {
    position: absolute;
    left: 40px;
    bottom: 44px;
    display: flex;
    align-items: center;
    gap: 12px;
  }
  .brand-mark {
    width: 16px;
    height: 16px;
    background: var(--ink);
  }
  .brand-name {
    font-weight: 800;
    font-size: 15px;
    line-height: 1.25;
    letter-spacing: 0.04em;
    text-transform: uppercase;
    color: var(--ink);
  }

  .holder {
    position: absolute;
    right: 40px;
    top: 46px;
    width: 260px;
  }
  .holder-name {
    font-weight: 300;
    font-size: 21px;
    letter-spacing: 0.03em;
    text-transform: uppercase;
    color: var(--ink);
  }
  .holder-role {
    margin-top: 4px;
    font-weight: 400;
    font-size: 11.5px;
    letter-spacing: 0.06em;
    text-transform: uppercase;
    color: var(--ink-soft);
  }
  .tri-rule {
    margin-top: 9px;
    display: flex;
    height: 2px;
    width: 260px;
  }
  .tri-rule span { flex: 1; }
  .tri-rule .rule-green { background: var(--accent-green); }
  .tri-rule .rule-red { background: var(--accent-red); }
  .tri-rule .rule-blue { background: var(--accent-blue); }

  .contact {
    position: absolute;
    right: 40px;
    top: 178px;
    width: 260px;
    list-style: none;
    font-size: 11.5px;
    font-weight: 400;
    color: var(--ink-soft);
    line-height: 1.65;
  }
  .contact-label {
    display: inline-block;
    width: 16px;
    color: var(--accent-red);
  }
</style>
</head>
<body>
  <main class="sheet">
    <section class="card card--reverse" aria-label="Card reverse">
      <span class="reverse-mark" aria-hidden="true"></span>
      <span class="reverse-name">Corvallin</span>
    </section>

    <section class="card card--front" aria-label="Card front">
      <div class="brand">
        <span class="brand-mark" aria-hidden="true"></span>
        <p class="brand-name">Corvallin<br>Property Solutions</p>
      </div>

      <div class="holder">
        <h1 class="holder-name">Marisol Dunkley</h1>
        <p class="holder-role">Property Investor</p>
        <div class="tri-rule" aria-hidden="true">
          <span class="rule-green"></span>
          <span class="rule-red"></span>
          <span class="rule-blue"></span>
        </div>
      </div>

      <ul class="contact">
        <li><span class="contact-label">m</span>+44(0)7700362517</li>
        <li><span class="contact-label">e</span>marisol.corvallin@quilbrook.example</li>
      </ul>
    </section>
  </main>
</body>
</html>
```